Commercial Bakery needs packing design for a Bread Bag.

Dorne's Bakery needs a design for a bread bag to be distributed to grocery stores. We make all kinds of breads and want this packaging to represent our company. We would like the packaging to be black and white with a fun/bubbly modern design. I have attached a few ideas of what I am looking for.
There are 5 different products. Packaging must be the same for each product except for corresponding product name, bar code and nutrional facts.
Product names:
Coconut Cream Bread
Cream Bread
Potato Rolls
Roll ups
Coconut & Raisin Bread

Our products are packaged in a 11” x 8” poly bag.
I will open 5 contracts with whoever’s design I select. I will then provide nutritional facts, barcodes for items once a contract is selected. Thank you!!

Target Market(s)

Grocery stores

Industry/Entity Type

Bakery

Requirements
Must have
• Black and White (off whites are ok)
Should not have
• Color

```html
<!DOCTYPE html>
<html lang="en">
<head>
<meta charset="utf-8">
<title>Dorne's Bakery – Coconut Cream Bread bag</title>
<link href="https://fonts.googleapis.com/css2?family=Bebas+Neue&family=Montserrat:wght@500&display=swap" rel="stylesheet">
<style>
  :root {
    --backdrop: #fdfcf8;
    --ink: #1c1c1c;
    --paper: #f7f7f5;
    --crumb-light: #f2d6a8;
    --crumb-dark: #c98a45;
    --rule: #8a8a8a;
  }
  * { box-sizing: border-box; margin: 0; padding: 0; }
  html, body { width: 1174px; height: 1200px; overflow: hidden; background: var(--backdrop); }
  .canvas { position: relative; width: 1174px; height: 1200px; }

  .bag-front {
    position: absolute; left: 302px; top: 50px;
    width: 570px; height: 1100px;
    border-radius: 14px; overflow: hidden;
  }
  .band { position: absolute; left: 0; width: 100%; background: var(--ink); }
  .band--top { top: 0; height: 100px; }
  .band--bottom { bottom: 0; height: 120px; }

  .loaf-window {
    position: absolute; left: 0; top: 100px; width: 100%; height: 880px;
    background: linear-gradient(100deg, var(--crumb-dark) 0%, var(--crumb-light) 30%, var(--crumb-light) 65%, var(--crumb-dark) 100%);
  }

  .label {
    position: absolute; left: 35px; top: 430px; width: 500px; height: 450px;
    background: var(--paper);
  }

  .brand-badge {
    position: absolute; left: 50%; top: 230px; transform: translateX(-50%);
    width: 240px; height: 240px; border-radius: 50%;
    background: var(--paper);
    display: flex; flex-direction: column; align-items: center; justify-content: center;
  }
  .brand-badge__ring {
    position: absolute; inset: 14px; border: 2px solid var(--ink); border-radius: 50%;
  }
  .brand-badge__name {
    font-family: "Bebas Neue", sans-serif; font-size: 58px; line-height: 1;
    color: var(--ink); letter-spacing: 1px; margin-top: 40px;
  }
  .brand-badge__sub {
    font-family: "Bebas Neue", sans-serif; font-size: 20px; letter-spacing: 3px;
    color: var(--ink); margin-top: 4px;
  }

  .product-name {
    position: absolute; left: 0; top: 108px; width: 100%;
    text-align: center; font-family: "Bebas Neue", sans-serif;
    font-size: 86px; line-height: 0.92; color: var(--ink); letter-spacing: 1px;
  }
  .product-rule {
    position: absolute; left: 60px; right: 60px; top: 292px;
    border-top: 1px solid var(--rule);
  }

  .grain-band {
    position: absolute; left: 0; bottom: 0; width: 100%; height: 145px;
    background: var(--ink);
  }
  .net-weight {
    position: absolute; left: 50%; bottom: 0; transform: translateX(-50%);
    background: var(--paper); padding: 6px 14px 2px;
    font-family: "Bebas Neue", sans-serif; font-size: 24px; color: var(--ink);
    letter-spacing: 0.5px;
  }
</style>
</head>
<body>
<main class="canvas">
  <section class="bag-front">
    <div class="band band--top"></div>
    <div class="loaf-window" role="img" aria-label="Photo of sliced white bread loaf seen through the bag"></div>
    <div class="band band--bottom"></div>

    <div class="label">
      <h1 class="product-name">Coconut<br>Cream Bread</h1>
      <div class="product-rule"></div>
      <div class="grain-band" role="img" aria-label="Decorative pattern of white wheat stalks on black">
      </div>
      <div class="net-weight">Net Wt. 16oz</div>
    </div>

    <div class="brand-badge">
      <div class="brand-badge__ring"></div>
      <span class="brand-badge__name">Dorne's</span>
      <span class="brand-badge__sub">Bakery</span>
    </div>
  </section>
</main>
</body>
</html>
```